Zippy Festivities!!! New business idea looking for proof of concept among customers

PERSONAL, FUN, EXCITING, MEMORABLE, UNIQUE
this is the idea for the business so I would like the brochure to portray this as well
I would like an eye catching design. The concept of the business is simple. We want to provide a personalized, memorable, unique and enjoyable experience and celebration for our clients as they chose to celebrate different events which may include but are not limited to (Birthday, holiday, anniversary, Special Event, no reason) for whomever it may be (friend, family member, significant other, coworker, frat/sorority brother/sister, etc) at a location of their choosing (on campus, public park, restaurant, bar etc). The celebration can take place at a private location or in a public scene where strangers can look on and take part in the fun. We will catch this act on video as well as take personalized photos and share it with the client for their own personal memories as well as utilize it on our own social media platforms. There are different packages that i would like to be included and most of the information id like to be included is attached. However, I would like to be able to add information or discard as necessary. The logo I would like to use is attached as well in three different designs. Designers may utilize the logo that they see fits their personal design the best! the logo with the flash in the background is one I personally like most but I am open to anything.
Just for visual of the concept. you want to surprise your friend with a Birthday blowout package for their birthday. The two of you are walking to class when your friend is shouted out by a DJ using a portable pa speaker system. Suddenly two confetti cannons go off, and your friend is overwhelmed with attention as well as personalized gifts given by strangers. Your friend as well as all onlookers are baffled to learn that you set up the whole experience just for them. Photos and videos have been taken throughout the whole experience to be shared with friends who weren't able to be their in person.
Designers you have the opportunity to be a part of a new, exciting and fun business. More than likely I will need a lot of things designed for the future of this business and I am looking to potentially develop a long-term partnership.
Target Market(s)
Ages 18-35. College students, Couples, office workers. Anybody celebrating anything.
Industry/Entity Type
Business
Requirements
Must have
- visuals that capture the attention of those viewing the brochure as well as providing a clear explanation of the concepts and packages. Packages must be easy to edit as pricing is not finalized. I would like the different packages to be on different pages with corresponding pictures in the panels or as background that still fit the overall theme. When you open the brochure the three panels should be Birthdays, Anniversaries, Other events, each with corresponding information from attached document

```html
<!DOCTYPE html>
<html lang="en">
<head>
<meta charset="utf-8">
<title>Zippy Festivities – Brochure</title>
<link rel="stylesheet" href="https://fonts.googleapis.com/css2?family=Didact+Gothic&display=swap">
<style>
  :root {
    --backdrop: #c9cacc;
    --paper: #ffffff;
    --magenta: #e5168a;
    --sun: #fff200;
    --ink: #2b2b2b;
    --ink-light: #ffffff;
    --brand-purple: #5b3f92;
    --link-blue: #3b4aa0;
    --cupcake-a: #d9a9c4;
    --cupcake-b: #7b5f86;
    --cupcake-c: #efc7d8;
    --gift-a: #c98ab8;
    --gift-b: #e7c9e0;
    --spark-a: #ffffff;
    --spark-b: #8e8a90;
    --spark-c: #3e3a40;
    --balloon-a: #ffffff;
    --balloon-b: #9a86c8;
    --balloon-c: #4d3a86;
  }
  * { box-sizing: border-box; margin: 0; padding: 0; }
  html, body { width: 1200px; height: 494px; overflow: hidden; }
  body {
    background: var(--backdrop);
    font-family: "Didact Gothic", "Century Gothic", sans-serif;
    color: var(--ink);
    position: relative;
  }
  .spread {
    position: absolute;
    top: 37px;
    width: 540px;
    height: 420px;
    display: flex;
    background: var(--paper);
  }
  .spread--inside { left: 40px; }
  .spread--outside { left: 620px; }
  .panel {
    position: relative;
    width: 180px;
    height: 100%;
    overflow: hidden;
    font-size: 5.4px;
    line-height: 1.32;
  }
  .panel + .panel { border-left: 1px solid #e6e6e6; }
  .panel__body { padding: 8px 9px; }
  .panel--magenta { background: var(--magenta); color: var(--ink-light); }
  .corner-flag {
    position: absolute; top: 0; right: 0; width: 26px; height: 26px;
  }
  .photo { display: block; width: 100%; }
  .photo--cupcakes {
    height: 100px;
    background: radial-gradient(circle at 30% 60%, var(--cupcake-c), transparent 40%),
                radial-gradient(circle at 70% 50%, var(--cupcake-b), transparent 45%),
                linear-gradient(120deg, var(--cupcake-a), var(--cupcake-b) 55%, var(--cupcake-c));
  }
  .photo--gift {
    position: absolute; bottom: 0; left: 0; height: 62px;
    background: linear-gradient(135deg, var(--gift-b), var(--gift-a) 60%, var(--gift-b));
  }
  .photo--sparkler {
    height: 292px;
    background: radial-gradient(circle at 55% 30%, var(--spark-a) 0 6%, transparent 22%),
                linear-gradient(180deg, var(--spark-c), var(--spark-b) 55%, var(--spark-a));
  }
  .photo--balloons {
    position: absolute; left: 0; bottom: 0; height: 300px;
    background: radial-gradient(circle at 70% 45%, var(--balloon-c), transparent 40%),
                radial-gradient(circle at 35% 70%, var(--balloon-b), transparent 45%),
                linear-gradient(180deg, var(--balloon-a), var(--balloon-b) 50%, var(--balloon-c));
  }
  .package-group { margin-bottom: 6px; }
  .section-title { font-size: 5.8px; margin-bottom: 5px; }
  .package-name { margin-top: 6px; }
  .list { list-style: none; }
  .list li { position: relative; padding-left: 8px; }
  .list--dot li::before { content: "•"; position: absolute; left: 1px; }
  .list--arrow li::before { content: "›"; position: absolute; left: 1px; }
  .list--arrow { margin-top: 4px; }
  .strong { font-weight: 700; -webkit-text-stroke: 0.15px currentColor; }
  .delivery-title { font-size: 8px; margin-bottom: 8px; }
  .delivery-item { font-size: 5.8px; margin-bottom: 8px; }
  .delivery-item b { display: block; -webkit-text-stroke: 0.2px currentColor; }
  .concept { margin: 8px 0; line-height: 1.45; }
  .form-field {
    border-bottom: 0.6px solid var(--ink-light);
    padding-top: 7px;
    padding-bottom: 3px;
  }
  .contact {
    text-align: center;
    color: var(--link-blue);
    padding-top: 20px;
    font-size: 5.4px;
    line-height: 2.4;
  }
  .contact__phone { font-size: 7px; }
  .brand-name {
    position: absolute; top: 24px; left: 0; width: 100%;
    text-align: center;
    font-size: 22px;
    line-height: 1.05;
    color: var(--brand-purple);
  }
</style>
</head>
<body>

<section class="spread spread--inside">
  <article class="panel panel--birthday">
    <div class="photo photo--cupcakes" role="img" aria-label="Photo of frosted cupcakes with sprinkles"></div>
    <div class="panel__body">
      <p class="section-title">Birthday Packages</p>
      <ul class="list list--arrow"><li>Requires Additional Fee's</li></ul>

      <p class="package-name">Basic Birthday ($99.99):</p>
      <ul class="list list--dot">
        <li>DJ Shout out + Music (to Birthday Boy/Girl including any special requests)</li>
        <li>Confetti (Streamers exploded through confetti cannon)</li>
        <li>One Dozen Balloons/or One Dozen Flowers</li>
        <li>Optional: Gift Presentation</li>
      </ul>
      <ul class="list list--arrow">
        <li>Photos/Videos ($5.00 per Photo/$10.00 Video/$49.99 Custom Video)</li>
        <li>Delivery Method (See Options)</li>
        <li>Additional instructions (Not Listed, Fees May Vary)</li>
      </ul>

      <p class="package-name">Better Birthday ($124.99):</p>
      <ul class="list list--dot">
        <li>DJ Shout out + Music (to Birthday Boy/Girl including any special requests)</li>
        <li>Confetti (Streamers exploded through confetti cannon)</li>
        <li>One Dozen Balloons/ or One Dozen Flowers</li>
        <li>Custom Birthday Cookie Cake (Grand Avenue Cookies)/ Birthday Sash &amp; Hat or Tiara</li>
        <li>Optional: Gift Presentation</li>
      </ul>
      <ul class="list list--arrow">
        <li>Photos/Videos ($5.00 per Photo/$10.00 Video/$49.99 Custom Video)</li>
        <li>Delivery Method (See Options)</li>
        <li>Additional Instructions (Not Listed)</li>
      </ul>

      <p class="package-name">Birthday Blowout ($199.99)</p>
      <ul class="list list--dot">
        <li>DJ Shout out + Music (to Birthday Boy/Girl including any special requests)</li>
        <li>Confetti (Streamers exploded through confetti cannon)</li>
        <li>One Dozen Balloons/ or One Dozen Flowers</li>
        <li>Custom Birthday Cookie Cake (Grand Avenue Cookies)</li>
        <li>Birthday Sash &amp; Hat/Tiara</li>
        <li>Free access to all Photos/Videos</li>
        <li>Choice of Delivery Method From Options</li>
        <li>Optional: Gift Presentation</li>
      </ul>
      <ul class="list list--arrow">
        <li>Custom Delivery (Not included in Options)</li>
        <li>Additional instructions (Not Listed)</li>
      </ul>
    </div>
  </article>

  <article class="panel panel--anniversary">
    <div class="photo photo--cupcakes" role="img" aria-label="Photo of frosted cupcakes, continued"></div>
    <div class="panel__body strong">
      <p class="section-title">Anniversary Packages</p>
      <ul class="list list--arrow"><li>Requires Additional Fee's</li></ul>

      <p class="package-name">Basic Aniversary ($99.99):</p>
      <ul class="list list--dot">
        <li>DJ Shout out + Music (to significant other including any special requests)</li>
        <li>Confetti/Rose petal confetti (Streamers exploded through confetti cannon)</li>
        <li>One Dozen Balloons/or One Dozen Flowers</li>
        <li>Optional: Gift Presentation</li>
      </ul>
      <ul class="list list--arrow">
        <li>Photos/Videos ($5.00 per Photo/$10.00 Video/$49.99 Custom Video)</li>
        <li>Delivery Method (See Options)</li>
        <li>Additional instructions (Not Listed, Fees May Vary)</li>
      </ul>

      <p class="package-name">Better Anniversary ($124.99):</p>
      <ul class="list list--dot">
        <li>DJ Shout out + Music (to significant other including any special requests)</li>
        <li>Confetti/Rose petal confetti (Streamers exploded through confetti cannon)</li>
        <li>One Dozen Balloons/ or One Dozen Flowers</li>
        <li>Custom Birthday Cookie Cake (Grand Avenue Cookies)/ Birthday Sash &amp; Hat or Tiara</li>
        <li>Optional: Gift Presentation</li>
      </ul>
      <ul class="list list--arrow">
        <li>Photos/Videos ($5.00 per Photo/$10.00 Video/$49.99 Custom Video)</li>
        <li>Delivery Method (See Options)</li>
        <li>Additional Instructions (Not Listed)</li>
      </ul>

      <p class="package-name">Anniversary Blowout ($199.99)</p>
      <ul class="list list--dot">
        <li>DJ Shout out + Music (to significant other including any special requests)</li>
        <li>Confetti/Rose petal confetti (Streamers exploded through confetti cannon)</li>
        <li>One Dozen Balloons/ or One Dozen Flowers</li>
        <li>Custom Birthday Cookie Cake (Grand Avenue Cookies)</li>
        <li>Birthday Sash &amp; Hat/Tiara</li>
        <li>Free access to all Photos/Videos</li>
        <li>Choice of Delivery Method From Options</li>
        <li>Optional: Gift Presentation</li>
      </ul>
      <ul class="list list--arrow">
        <li>Custom Delivery (Not included in Options)</li>
        <li>Additional instructions (Not Listed)</li>
      </ul>
    </div>
  </article>

  <article class="panel panel--magenta panel--other-events">
    <svg class="corner-flag" viewBox="0 0 26 26" aria-hidden="true"><polygon points="0,0 26,0 26,26" fill="var(--sun)"/></svg>
    <div class="panel__body">
      <p class="section-title">Other Events Packages</p>
      <p>including but not limited to:</p>
      <ul class="list list--dot">
        <li>bachelor/bachelorette parties</li>
        <li>holiday parties</li>
        <li>breakups/makeups</li>
        <li>feel good moments</li>
        <li>embarrass your friends/coworkers</li>
        <li>office parties</li>
      </ul>
      <ul class="list list--arrow"><li>Requires Additional Fee's</li></ul>

      <p class="package-name">Basic ($99.99):</p>
      <ul class="list list--dot">
        <li>DJ Shout out + Music (including any special requests)</li>
        <li>Confetti (Streamers exploded through confetti cannon)</li>
        <li>One Dozen Balloons/or One Dozen Flowers</li>
        <li>Optional: Gift Presentation</li>
      </ul>
      <ul class="list list--arrow">
        <li>Photos/Videos ($5.00 per Photo/$10.00 Video/$49.99 Custom Video)</li>
        <li>Delivery Method (See Options)</li>
        <li>Additional instructions (Not Listed, Fees May Vary)</li>
      </ul>

      <p class="package-name">Better ($124.99):</p>
      <ul class="list list--dot">
        <li>DJ Shout out + Music (to Birthday Boy/Girl including any special requests)</li>
        <li>Confetti (Streamers exploded through confetti cannon)</li>
        <li>One Dozen Balloons/ or One Dozen Flowers</li>
        <li>Custom Birthday Cookie Cake (Grand Avenue Cookies)/ Birthday Sash &amp; Hat or Tiara</li>
        <li>Optional: Gift Presentation</li>
      </ul>
      <ul class="list list--arrow">
        <li>Photos/Videos ($5.00 per Photo/$10.00 Video/$49.99 Custom Video)</li>
        <li>Delivery Method (See Options)</li>
        <li>Additional Instructions (Not Listed)</li>
      </ul>

      <p class="package-name">Blowout ($199.99)</p>
      <ul class="list list--dot">
        <li>DJ Shout out + Music (to Birthday Boy/Girl including any special requests)</li>
        <li>Confetti (Streamers exploded through confetti cannon)</li>
        <li>One Dozen Balloons/ or One Dozen Flowers</li>
        <li>Custom Birthday Cookie Cake (Grand Avenue Cookies)</li>
        <li>Birthday Sash &amp; Hat/Tiara</li>
        <li>Free access to all Photos/Videos</li>
        <li>Choice of Delivery Method From Options</li>
        <li>Optional: Gift Presentation</li>
      </ul>
      <ul class="list list--arrow">
        <li>Custom Delivery (Not included in Options)</li>
        <li>Additional instructions (Not Listed)</li>
      </ul>
    </div>
    <div class="photo photo--gift" role="img" aria-label="Photo of wrapped gift boxes with ribbon"></div>
  </article>
</section>

<section class="spread spread--outside">
  <article class="panel panel--magenta panel--delivery">
    <svg class="corner-flag" viewBox="0 0 26 26" aria-hidden="true"><polygon points="0,0 26,0 26,26" fill="var(--sun)"/></svg>
    <div class="panel__body">
      <p class="delivery-title">Delivery Options</p>
      <p class="delivery-item">Standard - Two Employees properly dressed for any occasion <b>Free</b></p>
      <p class="delivery-item">Ladies – Two females dressed in party attire <b>$24.99</b></p>
      <p class="delivery-item">Gents – Two males dressed in party attire <b>$24.99</b></p>
      <p class="delivery-item">Ladys N Gents – Male(s) and Female(s) <b>(2) $24.99 | (4) $39.99</b></p>
      <p class="delivery-item">Custom Costume - Characters, outfits &amp; special requests <b>(IF ATTAINABLE)</b> <b>Price Varies</b></p>
      <p class="concept">The concept of the business is simple. We want to provide a personalized, memorable, unique and enjoyable experience and celebration for our clients as they chose to celebrate different events which may include but are not limited to (Birthday, holiday, anniversary, Special Event, no reason) for whomever it may be (friend, family member, significant other, coworker, frat/sorority brother/sister, etc) at a location of their choosing (on campus, public park, restaurant, bar etc). The celebration can take place at a private location or in a public scene where strangers can look on and take part in the fun. We will catch this act on video as well as take personalized photos and share it with the client for their own personal memories as well as utilize it on our own social media platforms.</p>
      <p>Please provide the following information:</p>
      <div class="booking-form">
        <p class="form-field">Customer Name:</p>
        <p class="form-field">Event Type:</p>
        <p class="form-field">Package:</p>
        <p class="form-field">Delivery Type:</p>
        <p class="form-field">Date/Time:</p>
        <p class="form-field">Location:</p>
        <p class="form-field">Additional notes:</p>
        <p class="form-field">Approximate Price budget:</p>
      </div>
    </div>
  </article>

  <article class="panel panel--contact">
    <div class="photo photo--sparkler" role="img" aria-label="Photo of a lit sparkler in a cake"></div>
    <div class="contact">
      <p class="contact__phone">Tel: 555-014-2876</p>
      <p>www.ZippyFestivities.example | hello@ZippyFestivities.example</p>
      <p>Friendspace.example/ZippyFestivities</p>
      <p>Snapwall.example/ZippyFestivities</p>
    </div>
  </article>

  <article class="panel panel--cover">
    <p class="brand-name">Zippy<br>Festivities</p>
    <div class="photo photo--balloons" role="img" aria-label="Photo of purple and white balloons"></div>
  </article>
</section>

</body>
</html>
```